Business Card Design Project

I want my business cards to stand and feel timeless! I also want people to get their hands on them and freak out over how cool these are, I already have a logo i just want a very cool card design! this is for a makeup artist and maybe one day a line of cosmetics.

Target Market(s)

I want this to target women from 18 to 45

Industry/Entity Type

Business

Font styles to use
Decorative
Script

Colors

Designer to choose colors to be used in the design.

Requirements
Must have
• it must be elegante

```html
<!DOCTYPE html>
<html lang="en">
<head>
<meta charset="utf-8">
<title>Mara Lune – Business Card</title>
<link href="https://fonts.googleapis.com/css2?family=Quicksand:wght@300;400;500&display=swap" rel="stylesheet">
<style>
  :root {
    --page-bg: #1c1c1e;
    --gold-light: #e8d27a;
    --gold: #c9a659;
    --gold-deep: #9a7a40;
    --blush: #c98f8a;
    --pink-text: #e0407a;
    --navy: #1d1d4a;
    --navy-deep: #15153a;
    --lavender: #8f8fb8;
    --white: #fbf8ee;
  }
  * { margin: 0; padding: 0; box-sizing: border-box; }
  html, body {
    width: 1200px; height: 900px; overflow: hidden;
    background: var(--page-bg);
    font-family: "Quicksand", sans-serif;
  }
  .stage {
    position: relative; width: 1200px; height: 900px;
    display: flex; align-items: center; justify-content: center; gap: 60px;
  }
  .card {
    position: relative; width: 520px; height: 297px;
    border-radius: 18px; overflow: hidden;
  }
  .photo-area { position: absolute; inset: 0; }

  /* Front */
  .card--front .photo-area {
    background: linear-gradient(135deg, var(--gold-deep), var(--blush) 40%, var(--gold-light));
  }
  .front-brand {
    position: absolute; left: 0; right: 0; top: 112px;
    text-align: center;
    font-weight: 300; font-size: 52px; letter-spacing: 8px;
    color: var(--white); line-height: 1;
  }
  .front-url {
    position: absolute; right: 60px; top: 190px;
    font-size: 16px; font-weight: 400; color: var(--pink-text);
  }

  /* Back */
  .card--back { background: var(--navy-deep); }
  .card--back .photo-area {
    background: linear-gradient(100deg, var(--navy-deep) 0%, var(--navy) 32%, var(--blush) 60%, var(--gold-light) 100%);
  }
  .contact {
    position: absolute; left: 36px; top: 60px; color: var(--gold-light);
  }
  .contact__name { font-size: 24px; font-weight: 400; }
  .contact__role { font-size: 14px; color: var(--pink-text); margin-top: 2px; }
  .contact__phone { font-size: 16px; margin-top: 22px; letter-spacing: 1px; }
  .contact__email { font-size: 14px; margin-top: 2px; }
  .contact__web { font-size: 14px; margin-top: 18px; }
  .back-brand {
    position: absolute; left: 36px; bottom: 36px;
    font-weight: 300; font-size: 32px; letter-spacing: 5px; color: var(--lavender);
  }
</style>
</head>
<body>
<main class="stage">
  <section class="card card--front">
    <div class="photo-area" role="img" aria-label="Photograph of soft out-of-focus gold and pink lights"></div>
    <div class="front-brand">MARA LUNE</div>
    <div class="front-url">www.makeupbymaralune.com</div>
  </section>

  <section class="card card--back">
    <div class="photo-area" role="img" aria-label="Photograph of out-of-focus gold and pink lights fading into navy"></div>
    <div class="contact">
      <div class="contact__name">Mara Lune</div>
      <div class="contact__role">Make Up Artist</div>
      <div class="contact__phone">123.XXX.XXXX</div>
      <div class="contact__email">mara@makeupbymaralune.com</div>
      <div class="contact__web">www.makeupbymaralune.com</div>
    </div>
    <div class="back-brand">MARA LUNE</div>
  </section>
</main>
</body>
</html>
```